Cover design for series of 4 Best Practice Guides

The Design Brief
We are looking for cover designs for a series of 4 industry Best Practice Guides (BPG):

1. Best Practice Guide: Repossessions
2. Best Practice Guide: Collections
3. Best Practice Guide: Investigations
4. Best Practice Guide: Process Serving

The only essential elements to be included in the design are:
1. our logo (attached in both blue and white - either is acceptable)
2. Publication Name

We are looking for a set of 4 clean and professional looking designs which are clearly linked/related but where each BPG is distinguishable as a different publication either by the use of colour or by the use of appropriate imagery (illustrations, appropriate photos etc).

The BPGs will be produced in both A4 hard copy and electronic format.

Files should be provided in either AI or PSD format.

Some Background Information
These BPGs are being produced by the Guild of Ledgerwick Brokers ([login to view URL]) an industry association in Australia representing collectors, investigators, process servers and repossession agents. Broadly known as mercantile agents, below is a brief description of each role:

o Collectors make demands for payment of overdue debts (often pursuant to a formal contract) and enter into dialogue with individual and corporate debtors in order to achieve resolution of delinquent accounts whether by full or part recovery or by establishing the debtor does not have the means to pay.

o Investigators inquire into, and obtain information about, the personal character or actions of persons, together with the character or nature of the business or occupation of any person.

o Process servers deliver court issued process for a variety of reasons including debt recovery, family law proceedings, civil and criminal litigation in strict accordance with the rules of the issuing court.

o Repossession agents act for principals to formal contracts (leases, bills of sale, hire purchase agreements etc.) to either seek payment of arrears or the balance of the loan facility or else to recover the security for the facility (cars, motor cycles etc.).

Below is an extract from the Repossession BPG:

INTRODUCTION: BEST PRACTICE GUIDE
The Guild of Ledgerwick Brokers is the industry association nationally representing businesses and persons engaged in collections, investigations, process serving and repossession services in Australia.
Membership of the GLB is voluntary - businesses and persons join to demonstrate their commitment to the high standards adopted and promoted by the association.

This Best Practice Guide sets out best practice standards expected from members involved in the provision of repossession services and which debtors and businesses engaging with members should expect. Members agree to comply with this Best Practice Guide by virtue of membership.

We believe that this Best Practice Guide will enable debtors and businesses to address their situation involving the repossession of goods in confidence of fair treatment by members. To fulfil the potential of this Best Practice Guide those with debts outstanding for which repossession of goods is involved must cooperate with the businesses managing their debts including the repossession of security items so as to agree to reasonable solutions.

This Best Practice Guide is intended as a helpful resource for debtors and creditors, whilst compliance by members is intended to ensure best practice standards are maintained.

```html
<!DOCTYPE html>
<html lang="en">
<head>
<meta charset="utf-8">
<title>Guild of Ledgerwick Brokers – Best Practice Guide Covers</title>
<link rel="stylesheet" href="https://fonts.googleapis.com/css2?family=Tenor+Sans&family=Open+Sans:wght@600;700&display=swap">
<style>
  :root {
    --page: #ffffff;
    --white: #ffffff;
    --purple: #8d0f5d;
    --purple-dark: #6e0a47;
    --purple-light: #a8207a;
    --green: #0f7a3e;
    --green-dark: #0a5c2e;
    --green-light: #1d9650;
    --blue: #213d91;
    --blue-dark: #172c6c;
    --blue-light: #3353ae;
    --red: #9e1a2b;
    --red-dark: #7c1220;
    --red-light: #bb2a3a;
  }
  * { margin: 0; padding: 0; box-sizing: border-box; }
  html, body { width: 866px; height: 1200px; overflow: hidden; background: var(--page); }
  .sheet { position: relative; width: 866px; height: 1200px; }

  .cover {
    position: absolute;
    width: 424px;
    height: 590px;
    overflow: hidden;
    background: linear-gradient(100deg, var(--c-dark) 0%, var(--c) 45%, var(--c-light) 100%);
  }
  .cover--investigations { left: 0; top: 0; --c: var(--purple); --c-dark: var(--purple-dark); --c-light: var(--purple-light); }
  .cover--collections { left: 442px; top: 0; --c: var(--green); --c-dark: var(--green-dark); --c-light: var(--green-light); }
  .cover--repossessions { left: 0; top: 610px; --c: var(--blue); --c-dark: var(--blue-dark); --c-light: var(--blue-light); }
  .cover--process { left: 442px; top: 610px; --c: var(--red); --c-dark: var(--red-dark); --c-light: var(--red-light); }

  .publisher {
    position: absolute; top: 32px; left: 0; width: 100%;
    text-align: center; color: var(--white);
    font-family: "Tenor Sans", sans-serif; font-size: 15px;
    font-variant: small-caps; letter-spacing: 0.3px;
  }

  .photo { position: absolute; left: 0; top: 40px; width: 424px; height: 192px; display: block; }

  .band { position: absolute; left: 0; top: 231px; width: 424px; height: 96px; background: var(--white); }

  .brand-dot {
    position: absolute; left: 150px; top: 264px; width: 30px; height: 30px;
    border-radius: 50%; background: var(--c);
  }

  .brand {
    position: absolute; left: 196px; top: 250px; width: 170px;
    text-align: left; color: var(--c);
    font-family: "Tenor Sans", sans-serif; font-size: 50px; letter-spacing: 6px; line-height: 58px;
  }

  .guide-label {
    position: absolute; left: 0; top: 427px; width: 311px; height: 67px;
    background: var(--white);
    display: flex; align-items: center; justify-content: center;
    color: var(--c-dark);
    font-family: "Tenor Sans", sans-serif; font-size: 25px; font-variant: small-caps;
    box-shadow: 0 2px 5px rgba(0,0,0,0.25);
  }

  .rule { position: absolute; left: 357px; top: 340px; width: 3px; height: 210px; background: var(--white); }

  .topic {
    position: absolute; left: 365px; bottom: 40px;
    writing-mode: vertical-rl; transform: rotate(180deg);
    color: var(--white);
    font-family: "Open Sans", sans-serif; font-weight: 700; font-size: 18px; letter-spacing: 1px;
  }
</style>
</head>
<body>
<main class="sheet">

  <section class="cover cover--investigations">
    <p class="publisher">Guild of Ledgerwick Brokers Limited</p>
    <svg class="photo" viewBox="0 0 424 192" role="img" aria-label="Photo of a camera zoom lens close up">
      <defs>
        <linearGradient id="photo-inv" x1="0" y1="0" x2="1" y2="0">
          <stop offset="0" stop-color="#3a2418"/>
          <stop offset="0.4" stop-color="#2a2a32"/>
          <stop offset="0.75" stop-color="#b7742f"/>
          <stop offset="1" stop-color="#e3a456"/>
        </linearGradient>
      </defs>
      <path d="M0,56 Q212,4 424,56" fill="none" stroke="rgba(255,255,255,0.35)" stroke-width="2"/>
      <path d="M0,58 Q212,6 424,58 L424,192 L0,192 Z" fill="url(#photo-inv)"/>
    </svg>
    <div class="band"></div>
    <div class="brand-dot"></div>
    <div class="brand">GLB</div>
    <div class="guide-label">Best Practice Guide</div>
    <div class="rule"></div>
    <div class="topic">INVESTIGATIONS</div>
  </section>

  <section class="cover cover--collections">
    <p class="publisher">Guild of Ledgerwick Brokers Limited</p>
    <svg class="photo" viewBox="0 0 424 192" role="img" aria-label="Photo of a golden dollar sign on a warm surface">
      <defs>
        <linearGradient id="photo-col" x1="0" y1="0" x2="1" y2="1">
          <stop offset="0" stop-color="#d9a45a"/>
          <stop offset="0.5" stop-color="#f0d2a0"/>
          <stop offset="1" stop-color="#b47a35"/>
        </linearGradient>
      </defs>
      <path d="M0,56 Q212,4 424,56" fill="none" stroke="rgba(255,255,255,0.35)" stroke-width="2"/>
      <path d="M0,58 Q212,6 424,58 L424,192 L0,192 Z" fill="url(#photo-col)"/>
    </svg>
    <div class="band"></div>
    <div class="brand-dot"></div>
    <div class="brand">GLB</div>
    <div class="guide-label">Best Practice Guide</div>
    <div class="rule"></div>
    <div class="topic">COLLECTIONS</div>
  </section>

  <section class="cover cover--repossessions">
    <p class="publisher">Guild of Ledgerwick Brokers Limited</p>
    <svg class="photo" viewBox="0 0 424 192" role="img" aria-label="Photo of house keys resting on a floor plan">
      <defs>
        <linearGradient id="photo-rep" x1="0" y1="0" x2="1" y2="0">
          <stop offset="0" stop-color="#9a9a9c"/>
          <stop offset="0.45" stop-color="#d8d8d4"/>
          <stop offset="1" stop-color="#e6d6c2"/>
        </linearGradient>
      </defs>
      <path d="M0,56 Q212,4 424,56" fill="none" stroke="rgba(255,255,255,0.35)" stroke-width="2"/>
      <path d="M0,58 Q212,6 424,58 L424,192 L0,192 Z" fill="url(#photo-rep)"/>
    </svg>
    <div class="band"></div>
    <div class="brand-dot"></div>
    <div class="brand">GLB</div>
    <div class="guide-label">Best Practice Guide</div>
    <div class="rule"></div>
    <div class="topic">REPOSSESSIONS</div>
  </section>

  <section class="cover cover--process">
    <p class="publisher">Guild of Ledgerwick Brokers Limited</p>
    <svg class="photo" viewBox="0 0 424 192" role="img" aria-label="Photo of a person being handed court documents">
      <defs>
        <linearGradient id="photo-pro" x1="0" y1="0" x2="1" y2="0">
          <stop offset="0" stop-color="#3a3030"/>
          <stop offset="0.3" stop-color="#e8e6e4"/>
          <stop offset="0.85" stop-color="#f4f2ef"/>
          <stop offset="1" stop-color="#8a7a6a"/>
        </linearGradient>
      </defs>
      <path d="M0,56 Q212,4 424,56" fill="none" stroke="rgba(255,255,255,0.35)" stroke-width="2"/>
      <path d="M0,58 Q212,6 424,58 L424,192 L0,192 Z" fill="url(#photo-pro)"/>
    </svg>
    <div class="band"></div>
    <div class="brand-dot"></div>
    <div class="brand">GLB</div>
    <div class="guide-label">Best Practice Guide</div>
    <div class="rule"></div>
    <div class="topic">PROCESS SERVING</div>
  </section>

</main>
</body>
</html>
```